Chinese Language Posters - TKUOME

We have created a series of African American heritage posters that will be distributed to Chinese Language Schools. We need a designer to create great posters for K-12 programs.

Quotes:
We have quotes from 6 important figures in Black History. We are seeking a designer to develop a poster utilizing at least one quote from each historical figure.

The designer MUST be fluent in Chinese in order to ensure the appropriate type and font.

Our organization, Tidewater Kestrel Union of Orchard Mentors Exchange, is a small organization of parents in the Bay Area working to encourage and support Black students learning the Chinese language.

Target Market(s)

These posters will be made available to Chinese Immersion schools (k-12).

Industry/Entity Type

Learning

Requirements
Must have
• Each poster should contain one quote from the list below.

Please create a poster of one historical figure and include their quote. The image can be abstract, landscape or an image of the figure.

The image should also include our logo. Our preferred logo is with the puffs but we understand if the clipart logo may be a better fit for the posters. (We LOVE the puffs logo though).
Nice to have
• I have uploaded images of each figure. The images can be used or a more abstract background. We are flexible. We would prefer a mix that includes figures and abstract backgrounds just focusing on the quote. We are open.

```html
<!DOCTYPE html>
<html lang="en">
<head>
<meta charset="utf-8">
<title>TKUOME Heritage Poster Series</title>
<link rel="stylesheet" href="https://fonts.googleapis.com/css2?family=Arimo:wght@400;700&family=Tinos&family=Noto+Serif+SC:wght@400&display=swap">
<style>
  :root {
    --page: #ffffff;
    --brown-dark: #2a1a08;
    --brown-mid: #6b4a16;
    --gold-text: #f0c63c;
    --green-dark: #0b2410;
    --green-mid: #2f6a22;
    --lime-text: #d9e24c;
    --red-dark: #2a0807;
    --red-mid: #6e1712;
    --amber-text: #e7a32c;
    --logo-red: #d52b22;
    --logo-text: #ffffff;
    --strip: #2b2b2b;
    --strip-edge: #4a4a4a;
    --strip-text: #cfcfcf;
  }
  * { margin: 0; padding: 0; box-sizing: border-box; }
  html, body { width: 800px; height: 1200px; overflow: hidden; background: var(--page); }
  body { position: relative; font-family: "Tinos", "Noto Serif SC", serif; }

  .poster { position: absolute; left: 124px; width: 558px; height: 394px; overflow: hidden; }
  .poster--educator { top: 1px; background: linear-gradient(90deg, var(--brown-dark) 0%, var(--brown-mid) 45%, #3a2609 100%); }
  .poster--minister { top: 402px; background: linear-gradient(90deg, var(--green-dark) 0%, var(--green-mid) 50%, #12361a 100%); }
  .poster--justice { top: 802px; background: linear-gradient(90deg, var(--red-dark) 0%, var(--red-mid) 55%, #3a0c09 100%); }

  .portrait { position: absolute; top: 0; bottom: 0; }
  .poster--educator .portrait { left: 0; width: 290px; background: radial-gradient(ellipse at 45% 40%, #c9a23a 0%, #6d531c 45%, #2e2109 85%); }
  .poster--minister .portrait { right: 0; width: 290px; background: radial-gradient(ellipse at 55% 40%, #a9c23a 0%, #3f6c1c 50%, #102a0f 90%); }
  .poster--justice .portrait { left: 0; width: 320px; background: radial-gradient(ellipse at 40% 45%, #e3a842 0%, #9a5a26 40%, #4a1a10 75%, transparent 95%); }

  .quote-block { position: absolute; text-align: center; }
  .quote-block p { font-size: 11.5px; line-height: 1.25; }
  .quote-block .zh { font-family: "Noto Serif SC", serif; font-size: 10.5px; margin-bottom: 12px; }
  .quote-block .author { font-size: 9.5px; margin-top: 2px; }
  .quote-block .author-zh { font-family: "Noto Serif SC", serif; font-size: 9px; }

  .poster--educator .quote-block { left: 230px; width: 300px; top: 96px; color: var(--gold-text); }
  .poster--minister .quote-block { left: 20px; width: 320px; top: 108px; color: var(--lime-text); }
  .poster--justice .quote-block { left: 260px; width: 220px; top: 197px; color: var(--amber-text); }

  .brand { position: absolute; display: flex; align-items: center; gap: 6px; }
  .brand-dot { width: 34px; height: 34px; border-radius: 50%; background: var(--logo-red); }
  .brand-name { font-family: "Arimo", sans-serif; font-size: 25px; font-weight: 400; color: var(--logo-text); line-height: 1; }
  .brand-tag { font-family: "Arimo", sans-serif; font-size: 4px; color: var(--logo-text); margin-top: 2px; white-space: nowrap; }
  .poster--educator .brand { left: 384px; top: 308px; }
  .poster--minister .brand { left: 18px; top: 306px; }
  .poster--justice .brand { left: 384px; top: 305px; }

  .figure-strip { position: absolute; bottom: 0; height: 28px; background: linear-gradient(180deg, var(--strip-edge), var(--strip)); display: flex; justify-content: space-around; align-items: center; border-radius: 6px 6px 0 0; }
  .figure-strip span { font-family: "Arimo", sans-serif; font-size: 7px; color: var(--strip-text); text-align: center; line-height: 1.2; }
  .figure-strip span em { font-style: normal; display: block; font-family: "Noto Serif SC", serif; }
  .poster--educator .figure-strip { left: 95px; right: 0; }
  .poster--minister .figure-strip { left: 0; width: 462px; }
  .strip-a { left: 0; width: 120px; }
  .strip-b { left: 188px; right: 0; }
</style>
</head>
<body>

<section class="poster poster--educator">
  <div class="portrait" role="img" aria-label="Sepia portrait photograph of Josiah Whitfield Crane in suit and bow tie"></div>
  <div class="quote-block">
    <p>When you do the common things in life in an uncommon way,<br>you will command the attention of the world.</p>
    <p class="zh">• 当你以不同寻常的方式做生活中寻常的事情，你将使世界为之瞩目。</p>
    <p>Education is the key to unlock the golden door of freedom.</p>
    <p class="zh">• 教育是打开金色自由之门的钥匙。</p>
    <p class="author">Josiah Whitfield Crane</p>
    <p class="author-zh">约西亚·克兰</p>
  </div>
  <div class="brand"><span class="brand-dot"></span><div><div class="brand-name">TKUOME</div><div class="brand-tag">Tidewater Kestrel Union of Orchard Mentors Exchange</div></div></div>
  <nav class="figure-strip">
    <span>Emmett Lyle Barrow<em>埃米特·巴罗</em></span>
    <span>Cornelius Ashby<em>科尼利厄斯·阿什比</em></span>
    <span>Desmond Q<em>德斯蒙德·Q</em></span>
    <span>Oduya<em>奥杜亚</em></span>
    <span>Nathaniel Bryce Holloway<em>纳撒尼尔·霍洛威</em></span>
  </nav>
</section>

<section class="poster poster--minister">
  <div class="portrait" role="img" aria-label="Green-toned photograph of Nathaniel Bryce Holloway leaning on a lectern"></div>
  <div class="quote-block">
    <p>Our lives begin to end the day we become silent about things that matter.</p>
    <p class="zh">我们对重要的事情沉默不语的那一天，就是我们人生结束的开始。</p>
    <p>I have a dream!</p>
    <p class="zh">我有一个梦想！</p>
    <p>Faith is taking the first step even when you don't see the whole staircase.</p>
    <p class="zh">信念就是踏出第一步，哪怕你看不到整个楼梯。</p>
    <p class="author">Nathaniel Bryce Holloway</p>
    <p class="author-zh">纳撒尼尔·霍洛威</p>
  </div>
  <div class="brand"><span class="brand-dot"></span><div><div class="brand-name">TKUOME</div><div class="brand-tag">Tidewater Kestrel Union of Orchard Mentors Exchange</div></div></div>
  <nav class="figure-strip">
    <span>Josiah Whitfield Crane<em>约西亚·克兰</em></span>
    <span>Emmett Lyle Barrow<em>埃米特·巴罗</em></span>
    <span>Cornelius Ashby<em>科尼利厄斯·阿什比</em></span>
    <span>Desmond Q<em>德斯蒙德·Q</em></span>
    <span>Oduya<em>奥杜亚</em></span>
  </nav>
</section>

<section class="poster poster--justice">
  <div class="portrait" role="img" aria-label="Amber-toned portrait photograph of Emmett Lyle Barrow in glasses, suit and tie"></div>
  <div class="quote-block">
    <p>What is the quality of your intent?</p>
    <p class="zh">你的意图真诚而与人为善吗？</p>
    <p class="author">Emmett Lyle Barrow</p>
    <p class="author-zh">埃米特·巴罗</p>
  </div>
  <div class="brand"><span class="brand-dot"></span><div><div class="brand-name">TKUOME</div><div class="brand-tag">Tidewater Kestrel Union of Orchard Mentors Exchange</div></div></div>
  <nav class="figure-strip strip-a">
    <span>Josiah Whitfield Crane<em>约西亚·克兰</em></span>
  </nav>
  <nav class="figure-strip strip-b">
    <span>Cornelius Ashby<em>科尼利厄斯·阿什比</em></span>
    <span>Desmond Q<em>德斯蒙德·Q</em></span>
    <span>Oduya<em>奥杜亚</em></span>
    <span>Nathaniel Bryce Holloway<em>纳撒尼尔·霍洛威</em></span>
  </nav>
</section>

</body>
</html>
```